Vehicle Rental Hire in the Algarve - Portugal

We are opening a Vehicle Rental company in the Algarve - Portugal - this will attract both locals and Tourists visiting. So we want this website to capture the beautiful location we will be set in, along with the familiarity of a vehicle rental company. And to keep a colour scheme in Line with out Logo. We are Marlenic Vehicle Rental.

Industry/Entity Type

Vehicle Rental

Number of Pages Required

1 page

Requirements
Must have
• must be professional, and simple to use navigation bar - must also have a "make a reservation" box - similar to the screenshot attached - Under our logo it must read "Vehicle Rental"
Nice to have
• It needs to be in a colour scheme that fits in with our logo

```html
<!DOCTYPE html>
<html lang="en">
<head>
<meta charset="utf-8">
<title>Marlenic Vehicle Rental</title>
<link href="https://fonts.googleapis.com/css2?family=Poppins:wght@400;500;600;700&display=swap" rel="stylesheet">
<style>
:root{
  --blue:#1d1ad6;
  --blue-deep:#1410b8;
  --red:#c9302a;
  --ink:#222;
  --muted:#666;
  --grey:#f4f4f4;
  --white:#fff;
}
*{margin:0;padding:0;box-sizing:border-box}
html,body{width:1200px;height:5372px;overflow:hidden}
body{font-family:'Poppins',sans-serif;color:var(--ink);background:var(--white);position:relative}
.abs{position:absolute}
.btn{display:inline-flex;align-items:center;gap:10px;font-weight:600;text-transform:uppercase;color:var(--white);font-size:12px;letter-spacing:.3px}
.btn svg{width:30px;height:10px}
.btn-red{background:var(--red)}
.btn-blue{background:var(--blue)}

/* header */
.site-header{position:absolute;top:0;left:0;width:1200px;height:113px;background:var(--white);z-index:5}
.logo-disc{position:absolute;left:64px;top:-40px;width:160px;height:190px;border-radius:0 0 80px 80px;background:var(--white);z-index:6;display:flex;flex-direction:column;align-items:center;justify-content:center;padding-top:30px}
.logo-name{font-size:25px;font-weight:700;color:var(--blue);letter-spacing:.5px}
.logo-tag{font-size:10px;font-weight:600;color:var(--blue);margin-top:2px}
.nav{position:absolute;right:70px;top:44px;display:flex;gap:38px;font-size:13px;color:#444}
.nav .active{color:var(--red);position:relative}
.nav .active::after{content:"";position:absolute;left:-4px;right:-4px;bottom:-12px;height:2px;background:var(--red)}

/* hero */
.hero{position:absolute;top:113px;left:0;width:1200px;height:695px;overflow:hidden}
.hero h1{position:absolute;left:77px;top:190px;color:var(--white);font-weight:700;font-size:62px;line-height:66px}
.hero h1 span{font-size:52px;font-weight:600;display:block}
.hero .cta{position:absolute;left:76px;top:425px;height:62px;padding:0 24px;font-size:15px}
.dots{position:absolute;left:276px;top:620px;display:flex;gap:5px}
.dots i{width:12px;height:12px;border-radius:50%;background:#a9a9dd}
.dots i:first-child{background:var(--white)}

/* reservation */
.reserve{position:absolute;left:768px;top:490px;width:360px;height:540px;background:var(--red);padding:28px 34px;color:var(--white);z-index:4}
.reserve h2{font-size:18px;font-weight:500;padding-bottom:6px;border-bottom:1px solid rgba(255,255,255,.7)}
.field-label{font-size:13px;margin:14px 0 6px}
.select{height:34px;background:var(--white);color:#888;font-size:11px;padding:0 12px;display:flex;align-items:center;justify-content:space-between}
.select::after{content:"";border:4px solid transparent;border-top:5px solid #333;margin-top:4px}
.check{font-size:12px;margin-top:10px;display:flex;align-items:center;gap:6px}
.check b{width:13px;height:13px;background:var(--white);display:inline-flex;align-items:center;justify-content:center}
.row2{display:flex;gap:12px}
.row2>div{flex:1}
.row2 .date::after{display:none}
.reserve .search{margin:18px auto 0;display:flex;width:142px;height:46px;justify-content:center}

/* about */
.about-photo{left:77px;top:933px;width:522px;height:649px;background:linear-gradient(135deg,#d7dadf,#f2f2f2 45%,#8d8f95 100%)}
.about-box{left:513px;top:1064px;width:540px;height:460px;background:var(--white);padding:60px 0 0 68px}
.about-box h2{font-size:44px;font-weight:500;color:var(--blue);line-height:1}
.about-box p{margin-top:30px;font-size:13px;line-height:27px;color:var(--muted);width:430px}
.about-box .btn{margin-top:44px;height:50px;padding:0 22px}

.section-title{position:absolute;left:0;width:1200px;text-align:center;font-size:48px;font-weight:500;color:var(--blue)}

/* steps */
.steps{left:95px;top:1808px;width:1010px;display:flex;justify-content:space-between}
.step{width:220px;text-align:center}
.step .ring{width:134px;height:134px;border:3px solid var(--red);border-radius:50%;margin:0 auto;display:flex;align-items:center;justify-content:center}
.step h3{margin-top:30px;font-size:18px;font-weight:600;color:var(--blue)}
.step p{margin-top:8px;font-size:13px;line-height:22px;color:var(--muted)}

/* vehicles */
.vehicles{left:0;top:2150px;width:1200px;height:1398px;background:var(--grey)}
.card{position:absolute;width:320px;height:505px;background:var(--white);box-shadow:0 0 14px rgba(0,0,0,.08);text-align:center;padding:8px}
.card .photo{height:290px}
.card h3{margin-top:36px;font-size:22px;font-weight:500}
.card .price{margin-top:10px;font-size:22px;font-weight:600;color:var(--red)}
.card .price small{font-size:13px;color:#333}
.card .btn{margin-top:20px;height:50px;padding:0 20px}

/* why */
.why{left:0;top:3548px;width:1200px;height:647px;background:var(--grey);overflow:hidden}
.why .red-panel{position:absolute;left:800px;top:0;width:400px;height:647px;background:var(--red)}
.why h2{position:absolute;left:75px;top:80px;font-size:52px;font-weight:500;color:var(--blue)}
.why .intro{position:absolute;left:75px;top:172px;width:600px;font-size:13px;line-height:26px;color:var(--muted)}
.feature{position:absolute;width:300px;padding-left:58px}
.feature svg{position:absolute;left:0;top:2px;width:42px;height:42px}
.feature h3{font-size:20px;font-weight:600;color:#111}
.feature p{margin-top:6px;font-size:13px;line-height:22px;color:var(--muted)}
.why .car{position:absolute;left:676px;top:220px;width:460px;height:280px;background:linear-gradient(135deg,#4d86d0,#1b4f9c 55%,#102f62)}

/* testimonials */
.quote{position:absolute;top:4424px;width:278px;height:278px;background:var(--white);box-shadow:0 0 16px rgba(0,0,0,.09);padding:38px 34px}
.stars{color:#f5b400;font-size:13px;letter-spacing:3px}
.quote p{margin-top:12px;font-size:12.5px;line-height:17px;color:#444;text-align:justify}
.who{position:absolute;left:34px;bottom:34px;display:flex;align-items:center;gap:12px;font-size:13px;font-weight:600}
.who i{width:56px;height:56px;border-radius:50%;background:#cfd3d8}

/* footer */
.footer{left:0;top:4890px;width:1200px;height:482px;background:var(--blue);color:var(--white)}
.newsletter{position:absolute;left:207px;top:56px;width:788px;height:108px;border-radius:54px;background:var(--red);display:flex;align-items:center;padding:0 24px 0 34px;gap:14px}
.newsletter h2{font-size:30px;font-weight:600;white-space:nowrap}
.news-input{flex:1;height:46px;background:var(--white);border-radius:23px;display:flex;align-items:center;justify-content:space-between;padding-left:20px;font-size:10px;color:#888}
.news-input span.go{height:46px;width:110px;border-radius:23px;background:var(--blue);color:var(--white);font-size:13px;font-weight:600;display:flex;align-items:center;justify-content:center}
.footer h4{position:absolute;top:215px;font-size:18px;font-weight:500}
.links{position:absolute;left:202px;top:258px;list-style:none;font-size:13px;line-height:26px}
.links li::before{content:"";display:inline-block;width:9px;height:9px;border-radius:50%;background:var(--red);margin-right:12px}
.foot-logo{position:absolute;left:466px;top:198px;width:220px;height:170px;border:2px solid var(--white);border-radius:50%;display:flex;flex-direction:column;align-items:center;justify-content:center}
.foot-logo b{font-size:32px;font-weight:700}
.foot-logo span{font-size:13px;font-weight:700;margin-top:4px}
.contact{position:absolute;left:773px;list-style:none;font-size:13px;line-height:16px}
.contact li{display:flex;gap:14px;align-items:center;margin-bottom:14px}
.contact li i{width:26px;height:26px;border:1.5px solid var(--white);border-radius:50%;flex:none;display:flex;align-items:center;justify-content:center}
.copyright{position:absolute;left:0;top:442px;width:1200px;height:40px;border-top:1px solid rgba(255,255,255,.3);display:flex;align-items:center;justify-content:space-between;padding:0 77px;font-size:11px}
.social{display:flex;gap:6px}
.social i{width:26px;height:26px;border:1.5px solid var(--white);border-radius:50%}
</style>
</head>
<body>

<header class="site-header">
  <div class="logo-disc">
    <div class="logo-name">MARLENIC</div>
    <div class="logo-tag">Vehicle Rental</div>
  </div>
  <nav class="nav">
    <span class="active">HOME</span><span>ABOUT US</span><span>HOW IT WORKS</span><span>GALLERY</span><span>BLOG</span><span>CONTACT US</span>
  </nav>
</header>

<section class="hero">
  <svg width="1200" height="695" viewBox="0 0 1200 695" style="position:absolute;left:0;top:0">
    <defs>
      <linearGradient id="heroPhoto" x1="0" y1="0" x2="1" y2="1">
        <stop offset="0" stop-color="#9ea3a6"/><stop offset=".5" stop-color="#3b3d42"/><stop offset="1" stop-color="#6c6e70"/>
      </linearGradient>
      <linearGradient id="heroBlue" x1="0" y1="0" x2="1" y2="0">
        <stop offset="0" stop-color="#2a20c9"/><stop offset="1" stop-color="#3a2fd8"/>
      </linearGradient>
    </defs>
    <rect width="1200" height="695" fill="url(#heroPhoto)" role="img" aria-label="Dark saloon car parked on a coastal road"/>
    <polygon points="0,0 735,0 540,695 0,695" fill="url(#heroBlue)"/>
    <polygon points="720,0 738,0 555,695 537,695" fill="var(--red)"/>
  </svg>
  <h1>RENTAL SERVICES<span>With A Wide Range</span><span>Of Vehicles</span></h1>
  <span class="btn btn-red cta">Get Started <svg viewBox="0 0 30 10"><path d="M0 5H28M23 1l5 4-5 4" stroke="#fff" stroke-width="1.6" fill="none"/></svg></span>
  <div class="dots"><i></i><i></i><i></i></div>
</section>

<form class="reserve">
  <h2>MAKE A RESERVATION</h2>
  <div class="field-label">Pick up location</div>
  <div class="select">Please Choose.....</div>
  <div class="check"><b><svg width="10" height="10" viewBox="0 0 10 10"><path d="M1 5l3 3 5-6" stroke="var(--blue)" stroke-width="2" fill="none"/></svg></b>Pick up location same as return location</div>
  <div class="field-label">Driver's age</div>
  <div class="select">Please Choose.....</div>
  <div class="field-label">Vehicle Category</div>
  <div class="select">All</div>
  <div class="row2">
    <div><div class="field-label">Pick up date</div><div class="select date">dd-mm-aaaa</div></div>
    <div><div class="field-label">Hour</div><div class="select">9:00</div></div>
  </div>
  <div class="row2">
    <div><div class="field-label">Drop off date</div><div class="select date">dd-mm-aaaa</div></div>
    <div><div class="field-label">Hour</div><div class="select">9:00</div></div>
  </div>
  <span class="btn btn-blue search">Search <svg viewBox="0 0 30 10"><path d="M0 5H28M23 1l5 4-5 4" stroke="#fff" stroke-width="1.6" fill="none"/></svg></span>
</form>

<div class="abs about-photo" role="img" aria-label="Rental agent handing over keys in a car showroom"></div>
<section class="abs about-box">
  <h2>ABOUT MARLENIC</h2>
  <p>Lorem ipsum dolor sit amet, consectetur adipiscing elit. Cras auctor semper ex, ac gravida odio convallis ut. Duis placerat venenatis justo at ultricies. Nullam purus felis, faucibus eu sagittis id, finibus in lorem. Curabitur ipsum odio, consectetur in tempor nec, gravida sit amet est. Nunc malesuada molestie libero, sed tincidunt lectus ut quam nec.</p>
  <span class="btn btn-red">Read More <svg viewBox="0 0 30 10"><path d="M0 5H28M23 1l5 4-5 4" stroke="#fff" stroke-width="1.6" fill="none"/></svg></span>
</section>

<h2 class="section-title" style="top:1700px">HOW IT WORKS</h2>
<div class="abs steps">
  <div class="step">
    <div class="ring"><svg width="80" height="50" viewBox="0 0 80 50"><path d="M8 34l6-14h20l8-10h16l8 10 6 4v10z" fill="var(--red)"/><rect x="36" y="4" width="10" height="6" fill="var(--blue)"/><circle cx="22" cy="36" r="7" fill="#333"/><circle cx="60" cy="36" r="7" fill="#333"/></svg></div>
    <h3>Select Your Vehicle</h3><p>Lorem ipsum dolor sit amet,<br>consectetur adipiscing.</p>
  </div>
  <div class="step">
    <div class="ring"><svg width="48" height="64" viewBox="0 0 48 64"><rect x="4" y="4" width="40" height="56" fill="var(--red)"/><g stroke="#fff" stroke-width="3"><path d="M12 18h24M12 26h24M12 34h24M12 42h24M12 50h24"/></g></svg></div>
    <h3>Book &amp; Confirm</h3><p>Lorem ipsum dolor sit amet,<br>consectetur adipiscing.</p>
  </div>
  <div class="step">
    <div class="ring"><svg width="66" height="48" viewBox="0 0 66 48"><rect x="2" y="2" width="62" height="44" rx="4" fill="var(--red)"/><rect x="10" y="12" width="18" height="14" fill="#fff"/><path d="M34 14h22M34 22h22M10 34h46" stroke="#fff" stroke-width="3"/></svg></div>
    <h3>Make A Payment</h3><p>Lorem ipsum dolor sit amet,<br>consectetur adipiscing.</p>
  </div>
  <div class="step">
    <div class="ring"><svg width="64" height="56" viewBox="0 0 64 56"><path d="M10 26l6-18h32l6 18h4v20H6V26z" fill="var(--red)"/><path d="M18 24l4-11h20l4 11z" fill="#fff"/><circle cx="16" cy="36" r="4" fill="#fff"/><circle cx="48" cy="36" r="4" fill="#fff"/><rect x="8" y="46" width="10" height="8" fill="var(--red)"/><rect x="46" y="46" width="10" height="8" fill="var(--red)"/></svg></div>
    <h3>Enjoy The Drive</h3><p>Lorem ipsum dolor sit amet,<br>consectetur adipiscing.</p>
  </div>
</div>

<section class="abs vehicles">
  <h2 class="section-title" style="top:120px">OUR RENTAL VEHICLES</h2>
  <div class="card" style="left:83px;top:219px"><div class="photo" role="img" aria-label="Black hatchback" style="background:linear-gradient(160deg,#b8b0a5,#2b2c30 60%,#555)"></div><h3>RENTAL VEHICLE 1</h3><div class="price">$35,99<small>/DAY</small></div><span class="btn btn-blue">View Details <svg viewBox="0 0 30 10"><path d="M0 5H28M23 1l5 4-5 4" stroke="#fff" stroke-width="1.6" fill="none"/></svg></span></div>
  <div class="card" style="left:440px;top:219px"><div class="photo" role="img" aria-label="White panel van" style="background:linear-gradient(160deg,#e6e6e6,#c9c9c9 55%,#8a8a8a)"></div><h3>RENTAL VEHICLE 2</h3><div class="price">$45,99<small>/DAY</small></div><span class="btn btn-blue">View Details <svg viewBox="0 0 30 10"><path d="M0 5H28M23 1l5 4-5 4" stroke="#fff" stroke-width="1.6" fill="none"/></svg></span></div>
  <div class="card" style="left:793px;top:219px"><div class="photo" role="img" aria-label="White sports coupe on a road at sunset" style="background:linear-gradient(180deg,#c9a58d,#e9e3df 55%,#545557)"></div><h3>RENTAL VEHICLE 3</h3><div class="price">$55,99<small>/DAY</small></div><span class="btn btn-blue">View Details <svg viewBox="0 0 30 10"><path d="M0 5H28M23 1l5 4-5 4" stroke="#fff" stroke-width="1.6" fill="none"/></svg></span></div>
  <div class="card" style="left:83px;top:753px"><div class="photo" role="img" aria-label="White SUV parked by a building" style="background:linear-gradient(160deg,#777,#d8d8d8 55%,#3e3e3e)"></div><h3>RENTAL VEHICLE 4</h3><div class="price">$35,99<small>/DAY</small></div><span class="btn btn-blue">View Details <svg viewBox="0 0 30 10"><path d="M0 5H28M23 1l5 4-5 4" stroke="#fff" stroke-width="1.6" fill="none"/></svg></span></div>
  <div class="card" style="left:440px;top:753px"><div class="photo" role="img" aria-label="Red compact car on a white background" style="background:linear-gradient(180deg,#f6eeee,#e4b9b7)"></div><h3>RENTAL VEHICLE 5</h3><div class="price">$45,99<small>/DAY</small></div><span class="btn btn-blue">View Details <svg viewBox="0 0 30 10"><path d="M0 5H28M23 1l5 4-5 4" stroke="#fff" stroke-width="1.6" fill="none"/></svg></span></div>
  <div class="card" style="left:793px;top:753px"><div class="photo" role="img" aria-label="Blue sports car on a white background" style="background:linear-gradient(180deg,#eef2f8,#b3c6e2)"></div><h3>RENTAL VEHICLE 6</h3><div class="price">$55,99<small>/DAY</small></div><span class="btn btn-blue">View Details <svg viewBox="0 0 30 10"><path d="M0 5H28M23 1l5 4-5 4" stroke="#fff" stroke-width="1.6" fill="none"/></svg></span></div>
</section>

<section class="abs why">
  <div class="red-panel"></div>
  <h2>WHY CHOOSE US?</h2>
  <p class="intro">Lorem ipsum dolor sit amet, consectetur adipiscing elit, sed do eiusmod tempor incidi dunt ut labore et dolore magna aliqua. Quis ipsum suspendisse ultrices gravida. Risus commodo viverra maecenas .</p>
  <div class="feature" style="left:75px;top:290px"><svg viewBox="0 0 42 42"><path d="M14 8h14l-4 6h-6zM10 40c-6 0-6-14 4-24h14c10 10 10 24 4 24z" fill="var(--red)"/><text x="21" y="34" font-size="14" font-weight="700" fill="#fff" text-anchor="middle" font-family="Poppins,sans-serif">$</text></svg><h3>Competitive Pricing</h3><p>Lorem ipsum dolor sit amet,<br>consectetur adipiscing elit.<br>Cras auctor semper ex, .</p></div>
  <div class="feature" style="left:385px;top:290px"><svg viewBox="0 0 42 42"><path d="M21 3l15 6v11c0 10-7 17-15 20C13 37 6 30 6 20V9z" fill="var(--red)"/><path d="M14 21l5 5 10-11" stroke="#fff" stroke-width="3" fill="none"/></svg><h3>Trusted Rent Service</h3><p>Lorem ipsum dolor sit amet,<br>consectetur adipiscing elit.<br>Cras auctor semper ex, .</p></div>
  <div class="feature" style="left:75px;top:423px"><svg viewBox="0 0 42 42"><path d="M6 36L30 12M36 6a7 7 0 0 0-8 9l-22 21 2 2 21-22a7 7 0 0 0 9-8l-5 4-3-1-1-3z" stroke="var(--red)" stroke-width="3" fill="none"/><path d="M8 6l26 30" stroke="var(--red)" stroke-width="4"/></svg><h3>Breakdown Asistance</h3><p>Lorem ipsum dolor sit amet,<br>consectetur adipiscing elit.<br>Cras auctor semper ex, .</p></div>
  <div class="feature" style="left:385px;top:423px"><svg viewBox="0 0 42 42"><circle cx="21" cy="16" r="9" fill="var(--red)"/><path d="M6 40c0-10 7-15 15-15s15 5 15 15z" fill="var(--red)"/><path d="M9 18a12 12 0 0 1 24 0" stroke="#333" stroke-width="2.5" fill="none"/></svg><h3>24/7 Support</h3><p>Lorem ipsum dolor sit amet,<br>consectetur adipiscing elit.<br>Cras auctor semper ex, .</p></div>
  <div class="car" role="img" aria-label="Blue sports car crossing into the red panel"></div>
</section>

<h2 class="section-title" style="top:4322px">WHAT OUR CLIENTS SAY</h2>
<div class="quote" style="left:148px"><div class="stars">★★★★★</div><p>Lorem ipsum dolor sit amet, conse ctetuer adipiscing elit. Aenean comodo ligula eget dolor. Aenean massa. Cum sociis</p><div class="who"><i role="img" aria-label="Client portrait"></i>Rafael Duarte</div></div>
<div class="quote" style="left:461px"><div class="stars">★★★★★</div><p>Lorem ipsum dolor sit amet, conse ctetuer adipiscing elit. Aenean comodo ligula eget dolor. Aenean massa. Cum sociis</p><div class="who"><i role="img" aria-label="Client portrait"></i>Clara Mendes</div></div>
<div class="quote" style="left:773px"><div class="stars">★★★★★</div><p>Lorem ipsum dolor sit amet, conse ctetuer adipiscing elit. Aenean comodo ligula eget dolor. Aenean massa. Cum sociis</p><div class="who"><i role="img" aria-label="Client portrait"></i>Tomas Ribeiro</div></div>
<span class="abs btn btn-red" style="left:523px;top:4753px;height:48px;padding:0 24px">View More <svg viewBox="0 0 30 10"><path d="M0 5H28M23 1l5 4-5 4" stroke="#fff" stroke-width="1.6" fill="none"/></svg></span>

<footer class="abs footer">
  <div class="newsletter">
    <h2>Our Newsletter Sign Up</h2>
    <div class="news-input">Enter Email Address<span class="go">SIGNUP</span></div>
  </div>
  <h4 style="left:202px">QUICK LINKS</h4>
  <ul class="links"><li>About Us</li><li>How It Works</li><li>Gallery</li><li>Blog</li><li>Contact Us</li></ul>
  <div class="foot-logo"><b>MARLENIC</b><span>Vehicle Rental</span></div>
  <h4 style="left:773px">CONTACT US</h4>
  <ul class="contact" style="top:262px">
    <li><i><svg width="12" height="12" viewBox="0 0 12 12"><path d="M2 1l3 1-1 2 3 3 2-1 1 3-2 2C4 11 1 8 0 3z" fill="#fff"/></svg></i><span>CALL US<br>0155 218 4420</span></li>
    <li><i><svg width="12" height="10" viewBox="0 0 12 10"><rect x=".5" y=".5" width="11" height="9" fill="none" stroke="#fff"/><path d="M.5 .5l5.5 5 5.5-5" stroke="#fff" fill="none"/></svg></i><span>EMAIL US<br>hello@marlenic-rental.pt</span></li>
    <li><i><svg width="10" height="13" viewBox="0 0 10 13"><path d="M5 13S0 7 0 5a5 5 0 0 1 10 0c0 2-5 8-5 8z" fill="#fff"/><circle cx="5" cy="5" r="2" fill="var(--blue)"/></svg></i><span>Address line here dummy<br>Address line here</span></li>
  </ul>
  <div class="copyright">
    <span>Copyright ©2024 - All Rights Reserved by Company name</span>
    <div class="social"><i></i><i></i><i></i><i></i></div>
  </div>
</footer>

</body>
</html>
```